Greek delicatessen shop Signage

We have a Greek delicatessen where we have three different large windows, where on the upper side of them, we would need three different window stickers of a similar theme. I have listed below the words we would like to be written on each different window sticker with all of these stickers needing an image to be included also which I have attached and named accordingly.

1st window (Dimensions 148cm width X 50cm height)
Wording underneath the attached logo (which is named 1st window) which must go first would be the following:
Premium olive oils, large cheese selection, retsina, ready meals, olives, wine, pasta, dolmades, pita bread, baklava, taramasalata, tzatziki, spanakopita, dried herbs, vinegars, spreads, beer, jams, tomato products, fruit preserves, cookies, breadsticks, halva, salts, mastic gum, dried fruit, coffee, tea etc etc
Ideally we would like the wording to start with large letters and get smaller as we go down the list and become infinit if possible.

Second window (Dimensions 148cm width X 50cm height) which must include the image of a souvlaki wrap (attachment named 2nd window-this can be cropped accordingly )
Wording would be the following:
Authentic Greek Souvlaki
-Gyros
-Chicken
-Vegeterian
Classic size $10.00
Jumbo size $15.00
Wednesday to Sunday 10.30am to 2.30pm

Third window (Dimensions 220cm width X 50cm height)
Wording underneath the logo named 3rd window would be the following.
Private venue available for Greek cooking lessons, birthday parties, corporate lunches, catering, team building and more. Ask our friendly staff for more information or call Marta at 027359260.

Target Market(s)

retail customers

Colors
34a7d7
3176b5
add136

Requirements
Nice to have
• Nice to have a playfull feel
Should not have
• would like to avoid Greek fonts and images of Greek monuments etc

```html
<!DOCTYPE html>
<html lang="en">
<head>
<meta charset="utf-8">
<title>Greek Delicatessen Window Stickers</title>
<link href="https://fonts.googleapis.com/css2?family=Share+Tech&family=Share+Tech+Mono&family=Playball&family=Cormorant+Garamond:ital,wght@0,600;1,600&family=Oswald:wght@400;500&family=Fira+Sans+Condensed:ital,wght@0,400;0,500;1,400&display=swap" rel="stylesheet">
<style>
  :root {
    --ink: #141414;
    --paper: #f7f7f6;
    --lime: #8cc63f;
    --green: #5fae45;
    --green-dark: #4a9a3a;
    --sky: #34a7d7;
    --blue: #3176b5;
    --orange: #f5874a;
    --gold: #f5b335;
    --peach: #ffc999;
    --red: #e64b35;
    --frame: #555;
    --photo-light: #f2c48f;
    --photo-mid: #d98a4a;
    --photo-dark: #9a4a28;
  }
  * { box-sizing: border-box; margin: 0; padding: 0; }
  html, body { width: 1200px; height: 1091px; overflow: hidden; background: #fff; }
  body { position: relative; font-family: "Share Tech", sans-serif; color: var(--ink); }

  .sticker {
    position: absolute;
    overflow: hidden;
    background: linear-gradient(180deg, #fbfbfa 0%, var(--paper) 60%, #efefed 100%);
  }
  .sticker--deli { left: 164px; top: 40px; width: 820px; height: 299px; border: 2px solid var(--frame); border-top-width: 1px; }
  .sticker--souvlaki { left: 164px; top: 361px; width: 821px; height: 299px; border-left: 1px solid var(--frame); border-bottom: 2px solid var(--frame); }
  .sticker--venue { left: 0; top: 712px; width: 1200px; height: 298px; border-top: 2px solid var(--frame); border-bottom: 2px solid var(--frame); }

  .sticker__art { position: absolute; inset: 0; width: 100%; height: 100%; }

  .brush-label {
    position: absolute;
    font-family: "Cormorant Garamond", serif;
    font-style: italic;
    font-weight: 600;
    color: #fff;
    letter-spacing: 1px;
    text-align: center;
    line-height: 1;
  }
  .script-title {
    position: absolute;
    font-family: "Playball", cursive;
    color: var(--ink);
    white-space: nowrap;
    line-height: 1;
  }

  /* deli */
  .brand { position: absolute; display: flex; align-items: center; gap: 8px; }
  .brand__dot { flex: none; width: 14px; height: 14px; border-radius: 50%; background: var(--green); }
  .brand__name { font-family: "Share Tech", sans-serif; font-size: 19px; color: var(--green-dark); white-space: nowrap; line-height: 1; }
  .brand--deli { left: 17px; top: 40px; }

  .product-list { position: absolute; list-style: none; font-family: "Share Tech Mono", monospace; font-size: 15.3px; line-height: 18.6px; letter-spacing: 0.5px; white-space: nowrap; }
  .product-list--a { left: 16px; top: 83px; }
  .product-list--b { left: 228px; top: 83px; }
  .product-list--c { left: 388px; top: 83px; }
  .initial { color: var(--lime); }

  /* souvlaki */
  .menu-list { position: absolute; left: 28px; top: 96px; list-style: none; font-size: 28px; line-height: 32px; }
  .hours-tag {
    position: absolute; left: 9px; top: 200px; width: 228px; height: 78px;
    background: var(--peach); transform: rotate(-3deg);
    font-family: "Fira Sans Condensed", sans-serif; font-size: 21px; line-height: 26px;
    padding: 12px 0 0 18px; white-space: nowrap;
  }
  .hours-tag__time { color: var(--green-dark); }

  .price-badge {
    position: absolute; border-radius: 50%; background: #fff; border: 6px solid var(--gold);
    display: flex; flex-direction: column; align-items: center; justify-content: center; text-align: center;
  }
  .price-badge__amount { font-family: "Oswald", sans-serif; font-size: 34px; color: var(--red); line-height: 1; letter-spacing: 0.5px; }
  .price-badge__size { font-family: "Cormorant Garamond", serif; font-weight: 600; font-size: 23px; line-height: 19px; margin-top: 6px; }
  .price-badge--classic { left: 441px; top: 19px; width: 126px; height: 126px; }
  .price-badge--jumbo { left: 317px; top: 168px; width: 126px; height: 126px; }

  /* venue */
  .brand--venue { left: 26px; top: 114px; gap: 10px; }
  .brand--venue .brand__dot { width: 22px; height: 22px; background: var(--blue); }
  .brand--venue .brand__name { font-size: 30px; color: var(--blue); }

  .service-list { position: absolute; left: 302px; top: 92px; list-style: none; font-size: 28px; line-height: 31.5px; white-space: nowrap; }
  .service-list__more { font-family: "Fira Sans Condensed", sans-serif; font-style: italic; font-size: 22px; margin-top: 2px; }

  .info-tag {
    position: absolute; left: 600px; top: 100px; width: 226px; height: 80px;
    background: var(--peach); transform: rotate(-3deg);
    font-family: "Fira Sans Condensed", sans-serif; font-size: 14.5px; line-height: 20px;
    padding: 16px 0 0 20px; white-space: nowrap;
  }
  .phone-plate {
    position: absolute; left: 507px; top: 204px; width: 364px; height: 75px;
    background: var(--green); display: flex; align-items: center; justify-content: center;
  }
  .phone-plate::before { content: ""; position: absolute; inset: 5px 12px; border: 1.5px solid rgba(255,255,255,0.6); }
  .phone-plate__number { font-family: "Oswald", sans-serif; font-weight: 500; font-size: 58px; color: #fff; letter-spacing: 3px; line-height: 1; }
</style>
</head>
<body>

<section class="sticker sticker--deli">
  <svg class="sticker__art" viewBox="0 0 820 298" preserveAspectRatio="none">
    <defs>
      <linearGradient id="deliPhoto" x1="0" y1="0" x2="1" y2="1">
        <stop offset="0" stop-color="var(--photo-light)"/>
        <stop offset="0.55" stop-color="var(--photo-mid)"/>
        <stop offset="1" stop-color="var(--photo-dark)"/>
      </linearGradient>
    </defs>
    <path d="M523,0 H820 V298 H496 C470,240 552,185 563,115 C570,60 540,30 523,0Z" fill="url(#deliPhoto)" role="img" aria-label="Photo of grilled pita breads with fries on a wooden board"/>
    <path d="M523,28 C560,80 572,150 540,198 C500,248 470,268 496,298" fill="none" stroke="var(--green)" stroke-width="6" stroke-linecap="round"/>
    <path d="M230,10 C280,2 340,4 372,14 L380,40 C330,36 280,40 226,44 L238,27Z" fill="var(--orange)"/>
    <path d="M0,282 C45,270 88,280 112,298 H0Z" fill="var(--gold)"/>
  </svg>

  <div class="brand brand--deli"><span class="brand__dot"></span><span class="brand__name">Olive Grove Deli</span></div>

  <div class="brush-label" style="left:230px;top:12px;width:150px;font-size:21px;">GREEK</div>
  <div class="script-title" style="left:215px;top:28px;font-size:44px;">Delicatessen</div>

  <ul class="product-list product-list--a">
    <li><span class="initial">P</span>remium olive oils</li>
    <li><span class="initial">L</span>arge cheese selection</li>
    <li><span class="initial">R</span>etsina</li>
    <li><span class="initial">R</span>eady meals</li>
    <li><span class="initial">O</span>lives</li>
    <li><span class="initial">W</span>ine</li>
    <li><span class="initial">P</span>asta</li>
    <li><span class="initial">D</span>olmades</li>
    <li><span class="initial">P</span>ita bread</li>
    <li><span class="initial">B</span>aklava</li>
  </ul>
  <ul class="product-list product-list--b">
    <li><span class="initial">T</span>aramasalata</li>
    <li><span class="initial">T</span>zatziki</li>
    <li><span class="initial">S</span>panakopita</li>
    <li><span class="initial">D</span>ried herbs</li>
    <li><span class="initial">V</span>inegars</li>
    <li><span class="initial">S</span>preads</li>
    <li><span class="initial">B</span>eer</li>
    <li><span class="initial">J</span>ams</li>
    <li><span class="initial">T</span>omato products</li>
    <li><span class="initial">F</span>ruit preserves</li>
  </ul>
  <ul class="product-list product-list--c">
    <li><span class="initial">C</span>ookies</li>
    <li><span class="initial">B</span>readsticks</li>
    <li><span class="initial">H</span>alva</li>
    <li><span class="initial">S</span>alts</li>
    <li><span class="initial">M</span>astic gum</li>
    <li><span class="initial">D</span>ried fruit</li>
    <li><span class="initial">C</span>offee</li>
    <li><span class="initial">T</span>ea</li>
  </ul>
</section>

<section class="sticker sticker--souvlaki">
  <svg class="sticker__art" viewBox="0 0 821 298" preserveAspectRatio="none">
    <defs>
      <linearGradient id="souvlakiPhoto" x1="0" y1="0" x2="1" y2="1">
        <stop offset="0" stop-color="var(--photo-mid)"/>
        <stop offset="0.5" stop-color="#c9673a"/>
        <stop offset="1" stop-color="#7a3a22"/>
      </linearGradient>
    </defs>
    <path d="M396,0 H821 V298 H378 C345,240 360,170 412,125 C438,95 420,40 396,0Z" fill="url(#souvlakiPhoto)" role="img" aria-label="Photo of a souvlaki pita wrap filled with meat, tomato, onion and tzatziki"/>
    <path d="M350,165 C365,140 385,125 410,112" fill="none" stroke="var(--green)" stroke-width="6" stroke-linecap="round"/>
    <path d="M395,0 C405,20 415,35 425,50" fill="none" stroke="var(--green)" stroke-width="5" stroke-linecap="round"/>
    <path d="M20,24 C90,4 190,0 240,14 L246,46 C180,40 100,48 16,54 L30,38Z" fill="var(--green)"/>
    <path d="M0,282 C45,270 88,280 112,298 H0Z" fill="var(--gold)"/>
  </svg>

  <div class="brush-label" style="left:60px;top:17px;width:150px;font-size:20px;">AUTHENTIC</div>
  <div class="script-title" style="left:17px;top:38px;font-size:48px;">Greek Souvlaki</div>

  <ul class="menu-list">
    <li><span class="initial">G</span>yros</li>
    <li><span class="initial">C</span>hicken</li>
    <li><span class="initial">V</span>egeterian</li>
  </ul>

  <div class="hours-tag">Wednesday to Sunday<br><span class="hours-tag__time">10.30am to 2.30pm</span></div>

  <div class="price-badge price-badge--classic">
    <span class="price-badge__amount">$10.00</span>
    <span class="price-badge__size">Classic<br>size</span>
  </div>
  <div class="price-badge price-badge--jumbo">
    <span class="price-badge__amount">$15.00</span>
    <span class="price-badge__size">Jumbo<br>size</span>
  </div>
</section>

<section class="sticker sticker--venue">
  <svg class="sticker__art" viewBox="0 0 1200 298" preserveAspectRatio="none">
    <defs>
      <linearGradient id="venuePhoto" x1="0" y1="0" x2="1" y2="1">
        <stop offset="0" stop-color="var(--photo-light)"/>
        <stop offset="0.55" stop-color="var(--photo-mid)"/>
        <stop offset="1" stop-color="var(--photo-dark)"/>
      </linearGradient>
    </defs>
    <path d="M940,0 H1200 V298 H905 C878,230 960,170 974,100 C982,50 952,20 940,0Z" fill="url(#venuePhoto)" role="img" aria-label="Photo of grilled pita breads, fries and a souvlaki wrap"/>
    <path d="M938,16 C970,60 980,120 950,170 C915,220 880,255 905,298" fill="none" stroke="var(--green)" stroke-width="6" stroke-linecap="round"/>
    <path d="M332,22 C390,6 460,4 496,14 L502,46 C450,40 390,46 326,52 L338,36Z" fill="var(--sky)"/>
    <path d="M0,252 C60,244 120,262 146,298 H0Z" fill="var(--gold)"/>
  </svg>

  <div class="brand brand--venue"><span class="brand__dot"></span><span class="brand__name">Marta's Kitchen</span></div>

  <div class="brush-label" style="left:345px;top:20px;width:150px;font-size:21px;">PRIVATE</div>
  <div class="script-title" style="left:280px;top:34px;font-size:44px;">Venue available for</div>

  <ul class="service-list">
    <li><span class="initial">G</span>reek cooking lessons</li>
    <li><span class="initial">B</span>irthday parties</li>
    <li><span class="initial">C</span>orporate lunches</li>
    <li><span class="initial">C</span>atering</li>
    <li><span class="initial">T</span>eam building</li>
    <li class="service-list__more">and more</li>
  </ul>

  <div class="info-tag">Ask our friendly staff for more<br>information or call Marta at</div>

  <div class="phone-plate"><span class="phone-plate__number">027359260</span></div>
</section>

</body>
</html>
```